Orva Business Card

we need a business card for flooring business called Orva Flooring, the design should be black and white. we have 2 locations

Carrowmere Showroom
527 Kellerman Road,
Carrowmere VIC 3187

Halsbury Showroom
462 Bramwell Hwy,
Halsbury VIC 3265

email : sales@orvaflooring.com.au
(03) 9471 2830

Please inform we sell , Laminate, Hybrid, Timber, carpet and commercial flooring

```html
<!DOCTYPE html>
<html lang="en">
<head>
<meta charset="utf-8">
<title>Orva Flooring – Business Card</title>
<link href="https://fonts.googleapis.com/css2?family=Poppins:wght@400&display=swap" rel="stylesheet">
<style>
  :root {
    --ink: #000000;
    --paper: #ffffff;
    --backdrop: #e2e0e1;
  }
  * { margin: 0; padding: 0; box-sizing: border-box; }
  html, body { width: 1200px; height: 1200px; overflow: hidden; }
  body {
    background: var(--backdrop);
    font-family: "Poppins", sans-serif;
    position: relative;
  }
  .card {
    position: absolute;
    left: 221px;
    width: 758px;
    height: 455px;
    background: var(--paper);
    box-shadow: 0 6px 14px rgba(0,0,0,0.28);
    overflow: hidden;
  }
  .card--front { top: 108px; }
  .card--back { top: 642px; }
  .card__split { position: absolute; inset: 0; width: 758px; height: 455px; }
  .brand {
    position: absolute;
    left: 50px;
    top: 150px;
    width: 218px;
    text-align: center;
    font-weight: 400;
    line-height: 1;
  }
  .brand__name { display: block; font-size: 88px; letter-spacing: 1px; }
  .brand__trade { display: block; font-size: 42px; margin-top: 28px; letter-spacing: 0.5px; }
  .brand--light { color: var(--paper); }
  .brand--dark { color: var(--ink); }
  .contact {
    position: absolute;
    left: 407px;
    top: 81px;
    color: var(--ink);
    font-size: 20px;
    line-height: 34px;
  }
  .contact__row { display: flex; align-items: flex-start; gap: 11px; margin-bottom: 10px; }
  .contact__row--address { margin-bottom: 12px; }
  .contact__icon { width: 29px; height: 29px; flex: none; margin-top: 2px; }
  .contact__text { white-space: nowrap; }
  .offer {
    position: absolute;
    right: 51px;
    top: 176px;
    width: 420px;
    text-align: right;
    color: var(--paper);
    font-size: 22px;
    line-height: 37px;
  }
</style>
</head>
<body>

<section class="card card--front">
  <svg class="card__split" viewBox="0 0 758 455" aria-hidden="true">
    <polygon points="0,0 150,0 477,455 0,455" fill="var(--ink)"/>
    <line x1="157" y1="0" x2="484" y2="455" stroke="var(--ink)" stroke-width="2.5"/>
  </svg>
  <div class="brand brand--light">
    <span class="brand__name">Orva</span>
    <span class="brand__trade">FLOORING</span>
  </div>
  <div class="contact">
    <div class="contact__row">
      <svg class="contact__icon" viewBox="0 0 29 29" aria-hidden="true">
        <circle cx="14.5" cy="14.5" r="13.5" fill="none" stroke="var(--ink)" stroke-width="1.4"/>
        <path d="M10 8.5 l2.5 -0.5 l1.3 3 l-1.6 1.2 q1.3 2.8 4 4 l1.2 -1.6 l3 1.3 l-0.5 2.5 q-6 0.5 -9.9 -9.9z" fill="none" stroke="var(--ink)" stroke-width="1.3" stroke-linejoin="round"/>
      </svg>
      <span class="contact__text">(03) 9471 2830</span>
    </div>
    <div class="contact__row">
      <svg class="contact__icon" viewBox="0 0 29 29" aria-hidden="true">
        <circle cx="14.5" cy="14.5" r="13.5" fill="none" stroke="var(--ink)" stroke-width="1.4"/>
        <rect x="8" y="10" width="13" height="9.5" fill="none" stroke="var(--ink)" stroke-width="1.3"/>
        <path d="M8 10 l6.5 5.5 l6.5 -5.5 M8 19.5 l5 -4.5 M21 19.5 l-5 -4.5" fill="none" stroke="var(--ink)" stroke-width="1.2"/>
      </svg>
      <span class="contact__text">sales@orvaflooring.com.au</span>
    </div>
    <div class="contact__row contact__row--address">
      <svg class="contact__icon" viewBox="0 0 29 29" aria-hidden="true">
        <circle cx="14.5" cy="14.5" r="13.5" fill="none" stroke="var(--ink)" stroke-width="1.4"/>
        <path d="M14.5 19 q-4.5 -4.5 -4.5 -7.5 a4.5 4.5 0 0 1 9 0 q0 3 -4.5 7.5z" fill="none" stroke="var(--ink)" stroke-width="1.3"/>
        <circle cx="14.5" cy="11.5" r="1.6" fill="var(--ink)"/>
        <ellipse cx="14.5" cy="20.5" rx="5" ry="1.5" fill="none" stroke="var(--ink)" stroke-width="1.1"/>
      </svg>
      <span class="contact__text">Carrowmere Showroom<br>527 Kellerman Road,<br>Carrowmere VIC 3187</span>
    </div>
    <div class="contact__row contact__row--address">
      <svg class="contact__icon" viewBox="0 0 29 29" aria-hidden="true">
        <circle cx="14.5" cy="14.5" r="13.5" fill="none" stroke="var(--ink)" stroke-width="1.4"/>
        <path d="M14.5 19 q-4.5 -4.5 -4.5 -7.5 a4.5 4.5 0 0 1 9 0 q0 3 -4.5 7.5z" fill="none" stroke="var(--ink)" stroke-width="1.3"/>
        <circle cx="14.5" cy="11.5" r="1.6" fill="var(--ink)"/>
        <ellipse cx="14.5" cy="20.5" rx="5" ry="1.5" fill="none" stroke="var(--ink)" stroke-width="1.1"/>
      </svg>
      <span class="contact__text">Halsbury Showroom<br>462 Bramwell Hwy,<br>Halsbury VIC 3265</span>
    </div>
  </div>
</section>

<section class="card card--back">
  <svg class="card__split" viewBox="0 0 758 455" aria-hidden="true">
    <line x1="151" y1="0" x2="478" y2="455" stroke="var(--ink)" stroke-width="2.5"/>
    <polygon points="158,0 758,0 758,455 485,455" fill="var(--ink)"/>
  </svg>
  <div class="brand brand--dark">
    <span class="brand__name">Orva</span>
    <span class="brand__trade">FLOORING</span>
  </div>
  <p class="offer">We sell, Laminate, Hybrid, Timber,<br>carpet and commercial<br>flooring</p>
</section>

</body>
</html>
```